Info-graphic design

We need an info-graphic created showing how to easily paint new timber furniture from scratch. Our product is kit set furniture that can be decorated by the user - offering them some flexibility in how the final product can look.

The info-graphic needs to be easy to follow and have a fun/interesting look. I have attached a document showing the text that needs to appear on the info-graphic. On the document I have marked in red where graphic icons of different things are required.

Paint

```html
<!DOCTYPE html>
<html lang="en">
<head>
<meta charset="utf-8">
<title>Get Started Painting</title>
<link rel="stylesheet" href="https://fonts.googleapis.com/css2?family=Montserrat:wght@600;700;800&family=Open+Sans:wght@400;600;700&display=swap">
<style>
:root{
  --teal:#1fb79b;
  --teal-dark:#179a82;
  --page:#eeeff0;
  --steel:#3f86a7;
  --steel-dark:#2e6b88;
  --navy:#23466a;
  --navy-deep:#1b3a58;
  --sky:#82c3e2;
  --text:#3f4a55;
  --muted:#5c6a76;
  --white:#ffffff;
}
*{box-sizing:border-box;margin:0;padding:0}
html,body{width:1200px;height:3388px;overflow:hidden}
body{background:var(--page);font-family:"Open Sans",Arial,sans-serif;color:var(--text);position:relative}
.header{position:absolute;left:0;top:0;width:1200px;height:272px;background:var(--teal);border-bottom:10px solid var(--teal-dark)}
.header-mark{position:absolute;left:52px;top:36px;width:200px;height:200px;background:var(--white);border-radius:20px 20px 60px 20px;opacity:.95}
.header-title{position:absolute;left:272px;top:44px;color:var(--white);font-family:"Montserrat",Arial,sans-serif;line-height:1}
.header-title .small{display:block;font-size:66px;font-weight:700;letter-spacing:1px}
.header-title .big{display:block;font-size:128px;font-weight:600;letter-spacing:2px;margin-top:-4px}
.banner{position:absolute;left:0;top:367px;width:1180px;height:140px}
.banner-text{position:absolute;left:36px;top:378px;font-family:"Montserrat",Arial,sans-serif;font-weight:700;font-size:48px;color:var(--white);letter-spacing:1px}
.tool{position:absolute;width:260px;text-align:center}
.tool-disc{width:186px;height:186px;border-radius:50%;background:var(--steel);margin:0 auto;position:relative}
.tool-num{position:absolute;left:-4px;top:-6px;width:58px;height:58px;border-radius:50%;background:var(--navy-deep);border:4px solid var(--page);color:var(--white);font-family:"Montserrat",Arial,sans-serif;font-weight:700;font-size:26px;line-height:50px;text-align:center}
.tool-label{margin-top:26px;font-size:20px;line-height:25px;color:var(--muted)}
.mdf{position:absolute;left:621px;top:1296px;width:551px;height:370px;background:var(--navy)}
.mdf-arrow{position:absolute;left:-34px;top:6px}
.mdf-inner{position:absolute;left:14px;top:14px;right:14px;bottom:14px;border:3px dashed rgba(255,255,255,.7);padding:18px 20px;color:var(--white);text-align:center}
.mdf-kicker{font-family:"Montserrat",Arial,sans-serif;font-weight:600;font-size:30px;text-align:right;margin-right:12px}
.mdf-head{font-family:"Montserrat",Arial,sans-serif;font-weight:800;font-size:32px;margin-top:2px}
.mdf-body{font-size:23px;line-height:29px;margin-top:2px}
.paints{position:absolute;left:155px;top:1750px;width:960px;height:240px;background:var(--sky);overflow:hidden}
.paints-body{position:absolute;left:80px;top:26px;right:30px;color:var(--white);font-size:22px;line-height:30px}
.paints-ribbon{position:absolute;left:40px;top:1690px;width:300px;height:300px;overflow:hidden}
.paints-ribbon span{position:absolute;left:-60px;top:74px;width:340px;height:74px;background:var(--steel-dark);transform:rotate(-40deg);color:var(--white);font-family:"Montserrat",Arial,sans-serif;font-weight:800;font-size:42px;line-height:74px;text-align:center;letter-spacing:2px}
.timeline{position:absolute;left:124px;top:2040px;width:6px;height:1290px;background:var(--navy)}
.step-disc{position:absolute;left:50px;width:155px;height:155px;border-radius:50%;background:var(--navy);border:6px solid var(--white);box-shadow:0 0 0 3px var(--navy)}
.step{position:absolute;left:282px;width:860px}
.step-title{font-family:"Montserrat",Arial,sans-serif;font-weight:800;font-size:29px;color:var(--navy)}
.step-body{font-size:20.5px;line-height:27px;color:var(--muted)}
.footer{position:absolute;left:0;top:3360px;width:1200px;height:28px;background:var(--teal)}
</style>
</head>
<body>

<header class="header">
  <div class="header-mark" role="img" aria-label="Paint brush icon"></div>
  <h1 class="header-title"><span class="small">GET STARTED</span><span class="big">PAINTING</span></h1>
</header>

<svg class="banner" width="1180" height="140" viewBox="0 0 1180 140">
  <polygon points="1040,34 1172,34 1140,87 1172,140 1040,140" fill="#23466a"/>
  <rect x="0" y="0" width="1100" height="118" fill="#3f86a7"/>
  <polygon points="1040,118 1100,118 1040,140" fill="#1b3a58"/>
</svg>
<div class="banner-text">REQUIRED</div>

<div class="tool" style="left:25px;top:550px"><div class="tool-disc" role="img" aria-label="Primer tin icon"><div class="tool-num">1</div></div><p class="tool-label">Primer/undercoat</p></div>
<div class="tool" style="left:308px;top:550px"><div class="tool-disc" role="img" aria-label="Paint tin icon"><div class="tool-num">2</div></div><p class="tool-label">Paint (topcoat)</p></div>
<div class="tool" style="left:590px;top:550px"><div class="tool-disc" role="img" aria-label="Sandpaper sheets icon"><div class="tool-num">3</div></div><p class="tool-label">Sandpaper/<br>sanding sponge<br>(120 and 220 grits),<br>or power sander<br>(optional)</p></div>
<div class="tool" style="left:872px;top:550px"><div class="tool-disc" role="img" aria-label="Brush and roller icon"><div class="tool-num">4</div></div><p class="tool-label">Paint brush,<br>mini roller,<br>or pad.</p></div>

<div class="tool" style="left:25px;top:946px"><div class="tool-disc" role="img" aria-label="Rags and solvent bottle icon"><div class="tool-num">5</div></div><p class="tool-label">Clean rags or cloth,<br>Solvent - for clean-up<br>if using oil-based<br>primer and paint</p></div>
<div class="tool" style="left:308px;top:946px"><div class="tool-disc" role="img" aria-label="Dust mask and goggles icon"><div class="tool-num">6</div></div><p class="tool-label">Dust mask<br>and goggles</p></div>
<div class="tool" style="left:590px;top:946px"><div class="tool-disc" role="img" aria-label="Latex glove icon"><div class="tool-num">7</div></div><p class="tool-label">Latex gloves<br>(optional)</p></div>
<div class="tool" style="left:872px;top:946px"><div class="tool-disc" role="img" aria-label="Ventilation fan icon"><div class="tool-num">8</div></div><p class="tool-label">Clean, safe, and<br>well-ventilated<br>working area</p></div>

<div class="tool" style="left:25px;top:1341px"><div class="tool-disc" role="img" aria-label="Drop sheet icon"><div class="tool-num">9</div></div><p class="tool-label">Use a drop sheet<br>to protect floors.</p></div>
<div class="tool" style="left:308px;top:1341px"><div class="tool-disc" role="img" aria-label="Work shirt icon"><div class="tool-num">10</div></div><p class="tool-label">Wear overalls, an apron,<br>or old clothes to avoid<br>getting your own<br>clothes messy</p></div>

<aside class="mdf">
  <svg class="mdf-arrow" width="36" height="60" viewBox="0 0 36 60"><polygon points="36,0 0,30 36,60" fill="#23466a"/></svg>
  <div class="mdf-inner">
    <p class="mdf-kicker">Before you start...</p>
    <p class="mdf-head">MDF</p>
    <p class="mdf-body">MDF is an absorbent and requires a primer or undercoat. This coat seals the MDF fibres and allows the topcoat to adhere to the board with good strength - resulting in a longer-lasting finish, and allowing a truer shade of the topcoat to show.</p>
  </div>
</aside>

<section class="paints">
  <p class="paints-body">Primers/undercoats can be acrylic/latex or oil based, acrylics are easier to work with and are ideal if you plan to use an acrylic-based paint for the topcoat. Acrylics can be thinned and cleaned up with water, which makes them less time-consuming to use, and are also friendlier to the environment. Oil-based primers give a more durable finish with better colour luminosity, but require mineral turpentine or other solvent to clean up.</p>
</section>
<div class="paints-ribbon"><span>PAINTS</span></div>

<div class="timeline"></div>
<div class="step-disc" style="top:2025px" role="img" aria-label="Window icon"></div>
<div class="step-disc" style="top:2280px" role="img" aria-label="Sanding icon"></div>
<div class="step-disc" style="top:2520px" role="img" aria-label="Sponge icon"></div>
<div class="step-disc" style="top:2746px" role="img" aria-label="Shield with tick icon"></div>
<div class="step-disc" style="top:2985px" role="img" aria-label="Painter with roller icon"></div>
<div class="step-disc" style="top:3197px" role="img" aria-label="Thumbs up icon"></div>

<div class="step" style="top:2040px"><h2 class="step-title">1. – START</h2><p class="step-body">Ensure you have a clean, tidy and safe working area. Put down drop sheets to protect floors. Your work area should be well-ventilated too.</p></div>
<div class="step" style="top:2250px"><h2 class="step-title">2. – PREPARE</h2><p class="step-body">Remove all dust &amp; debris from the MDF surface. Use a rough-grit sandpaper such as 120 grit to do this. Then use a finer grit sandpaper to achieve a finish that isn't too rough, but will allow the undercoat to adhere to the surface. Pay special attention to the edges and ensure they are smooth so the primer will adhere and not soak up too much.</p></div>
<div class="step" style="top:2486px"><h2 class="step-title">3. – CLEAN</h2><p class="step-body">Use a damp cloth to clean the MDF surface(s) once sanded. This will ensure there are no loose particles on the surface and keep the undercoat adhered to the surface. MDF produces a fine dust when sanded, so take extra care to clean up all dust particles – for this step, it might be best to do this before the furniture is assembled. Allow the MDF to dry completely before beginning the next step.</p></div>
<div class="step" style="top:2730px"><h2 class="step-title">4. – SEAL</h2><p class="step-body">Apply a coat of primer. When the surface has dried fully, sand with a fine sandpaper (220 grit). Apply a second coat of primer. Ensure the edges of the MDF are sealed well, as these are the areas most likely to absorb moisture.</p></div>
<div class="step" style="top:2966px"><h2 class="step-title">5. – TOPCOATS</h2><p class="step-body">Once the primer has dried fully, you can move onto applying the topcoats. It is recommended that if you have used an acrylic primer, then use an acrylic topcoat. Likewise, if you have used an oil-based primer, use an oil based top coat. Avoid overloading brush or roller with paint. Apply a thin coat first, allow to dry then sand lightly. Again use a damp cloth to clean-up all dust. Apply a second coat. It's best to coat both sides of the MDF to help prevent any bowing of the board after the paint has dried.</p></div>
<div class="step" style="top:3196px"><h2 class="step-title">6. – FINISH</h2><p class="step-body">Allow paint to fully dry/cure (refer to manufacturers instructions for drying time). Dispose of any leftover paint responsibly.</p></div>

<div class="footer"></div>
</body>
</html>
```